Book cover for a book about time management for women

We need a book cover for a book about time management for women written by a woman. Even though the book has a provocative title "Calendar candy" based on the seminars the author holds for women seeking the change in their life, it has nothing to do with the words themselves. The subtitle is "Keep each morning in your grip. A bold guide on daily rhythm for ladies today"

Preferred fonts (not necessarily):
Plus Jakarta Sans
Tiempos Headline

Preferred colours (not necessarily):
- orange
- pastel "highlighters"

We look for a simple/clean design that catches the attention of the women without too many graphic elements.

Target Market(s)

Women that want to change and organise their life

Industry/Entity Type

productivity, marketing, work-life balance

Font styles to use
Other font styles liked:
• Plus Jakarta Sans, Tiempos Headline

Colors
F0912C
F2A743
F7CA91
FBE8D2
FDF5EE
A7469A
B969AE
D3A5CF
EDDBEB
F8F0F9

Requirements
Must have
• Famine feeling as the target audience are women with drive to better life
Should not have
• No explicit images or sexually motivated themes

```html
<!DOCTYPE html>
<html lang="en">
<head>
<meta charset="utf-8">
<title>Calendar Candy — Book Cover</title>
<link rel="stylesheet" href="https://fonts.googleapis.com/css2?family=Plus+Jakarta+Sans:wght@300;800&family=Libre+Baskerville:wght@400&family=Source+Serif+4:opsz,wght@8..60,500&display=swap">
<style>
  :root {
    --page: #ffffff;
    --cover-top: #f6b51f;
    --cover-bottom: #f4ad1c;
    --ink: #1f1d1a;
    --white: #ffffff;
    --accent: #f0912c;
    --photo-light: #e4e2de;
    --photo-mid: #b3b1ad;
    --photo-dark: #8f8d8a;
  }
  * { margin: 0; padding: 0; box-sizing: border-box; }
  html, body {
    width: 1200px; height: 1200px; overflow: hidden;
    background: var(--page);
  }
  .cover {
    position: absolute; left: 203px; top: 0;
    width: 797px; height: 1200px;
    background: linear-gradient(180deg, var(--cover-top), var(--cover-bottom));
    box-shadow: 0 0 14px rgba(0,0,0,.35);
    overflow: hidden;
  }
  .kicker {
    position: absolute; top: 64px; left: 0; width: 100%;
    text-align: center;
    font-family: "Libre Baskerville", Georgia, serif;
    font-size: 24px; line-height: 36px; letter-spacing: 4.4px;
    color: var(--ink);
  }
  .title-top {
    position: absolute; top: 170px; left: 0; width: 100%;
    text-align: center;
    font-family: "Plus Jakarta Sans", Arial, sans-serif;
    font-weight: 300; font-size: 76px; letter-spacing: 6px;
    color: var(--white); line-height: 1;
  }
  .title-main {
    position: absolute; top: 270px; left: 52px; width: 694px; height: 196px;
    display: flex; align-items: center; justify-content: space-between;
    font-family: "Plus Jakarta Sans", Arial, sans-serif;
    font-weight: 800; font-size: 176px; line-height: 1;
    color: var(--white);
  }
  .title-main > span { flex-shrink: 0; }
  .tagline-disc {
    flex: 0 0 190px;
    width: 190px; height: 190px; border-radius: 50%;
    background: var(--white);
    box-shadow: 0 0 22px rgba(255,255,255,.9);
    display: flex; flex-direction: column; align-items: center; justify-content: center;
    font-family: "Source Serif 4", Georgia, serif;
    font-weight: 500; font-size: 25px; line-height: 30px;
    color: var(--ink); text-align: center; letter-spacing: -0.5px;
    white-space: nowrap;
  }
  .tagline-disc .highlight { color: var(--accent); }
  .author {
    position: absolute; top: 480px; right: 55px;
    font-family: "Libre Baskerville", Georgia, serif;
    font-size: 42px; letter-spacing: 7px; line-height: 1;
    color: var(--ink);
  }
  .cover-photo {
    position: absolute; left: 150px; top: 548px;
    width: 490px; height: 652px;
  }
</style>
</head>
<body>
  <div class="cover">
    <p class="kicker">A BOLD GUIDE ON DAILY RHYTHM<br>FOR LADIES TODAY</p>
    <h1 class="title-top">CALENDAR</h1>
    <div class="title-main" aria-label="Candy">
      <span>C</span>
      <div class="tagline-disc">
        <span>Keep</span>
        <span class="highlight">each morning</span>
        <span>in your</span>
        <span>grip</span>
      </div>
      <span>N</span><span>D</span><span>Y</span>
    </div>
    <p class="author">AUTHOR NAME</p>
    <svg class="cover-photo" viewBox="0 0 490 652" role="img" aria-label="Photo of a girl in a grey sweater holding a large wall clock in front of her face">
      <defs>
        <linearGradient id="photo-tone" x1="0" y1="0" x2="0" y2="1">
          <stop offset="0" stop-color="var(--photo-light)"/>
          <stop offset="0.55" stop-color="var(--photo-mid)"/>
          <stop offset="1" stop-color="var(--photo-dark)"/>
        </linearGradient>
      </defs>
      <rect x="0" y="0" width="490" height="652" rx="24" fill="url(#photo-tone)" opacity=".85"/>
    </svg>
  </div>
</body>
</html>
```